Redesign Of Flower Delivery Subscription Service Website

I need a revamped website of www.petal-rush.com

Please revamp current design using same content....

Target Market(s)

people who buy flowers. Brides, wedding planners, wedding photographer, married man, boyfriend, etc.

Industry/Entity Type

Florist

Number of Pages Required

5+ page

Colors

Designer to choose colors to be used in the design.

Requirements
Must have
• I need a revamped website of www.petal-rush.com
• Please revamp current design using same content....
Nice to have
Should not have

```html
<!DOCTYPE html>
<html lang="en">
<head>
<meta charset="utf-8">
<title>Petal Rush – Monthly Flower Subscription</title>
<link rel="stylesheet" href="https://fonts.googleapis.com/css2?family=Dancing+Script:wght@600;700&family=Jost:wght@400;500&family=Poppins:wght@500;600&display=swap">
<style>
:root{
  --green:#8cc63f;
  --green-soft:#b6df88;
  --mint:#eef6e3;
  --ink:#1e1e1e;
  --text:#6a6a6a;
  --muted:#8a8a8a;
  --line:#d9dfd2;
  --white:#ffffff;
}
*{margin:0;padding:0;box-sizing:border-box}
html,body{width:1200px;height:3125px;overflow:hidden;background:var(--white)}
body{position:relative;font-family:"Jost",sans-serif;color:var(--text)}
.abs{position:absolute}
.script{font-family:"Dancing Script",cursive;font-weight:700;color:var(--ink)}

/* top bar */
.topbar-links{left:79px;top:10px;font-size:13px;color:var(--muted);display:flex;gap:16px}
.topbar-links span.sep{color:#ccc}
.buy-now{left:875px;top:9px;font-size:14px;color:var(--ink);display:flex;align-items:center;gap:8px;text-decoration:underline}
.social-top{top:12px;width:12px;height:12px;border-radius:50%;background:var(--green)}
.topbar-rule{left:0;top:42px;width:1200px;height:1px;background:#eee}

/* nav */
.logo{left:79px;top:66px;display:flex;align-items:center;gap:10px;font-size:30px;font-weight:500;color:var(--green)}
.logo-dot{width:22px;height:22px;border-radius:50%;background:var(--green)}
.nav{left:315px;top:77px;display:flex;gap:0;font-size:15px;color:#333}
.nav a{position:absolute;white-space:nowrap;text-decoration:none;color:#333}
.nav a.active{color:var(--green)}
.search{left:1085px;top:69px;width:38px;height:38px;border-radius:50%;background:var(--green);display:flex;align-items:center;justify-content:center}

/* hero */
.hero{left:0;top:135px;width:1200px;height:584px;background:var(--mint)}
.hero-title{left:79px;top:290px;font-size:54px;font-weight:600;font-style:italic}
.hero-sub{left:79px;top:380px;font-size:15px;line-height:26px;color:#555}
.btn{height:41px;border-radius:21px;font-size:15px;font-family:"Poppins",sans-serif;font-weight:600;display:flex;align-items:center;justify-content:center}
.btn-fill{left:79px;top:469px;width:144px;background:var(--green);color:var(--ink)}
.btn-line{left:233px;top:469px;width:146px;border:2px solid var(--green-soft);color:var(--green);background:var(--white)}
.photo{display:block}

/* feature photos */
.caption{font-size:21px;text-align:center;width:312px}

/* subscribe */
.subscribe{left:0;top:1135px;width:1200px;height:375px;background:var(--mint)}
.sub-title{left:79px;top:1228px;font-size:36px}
.sub-text{left:79px;top:1300px;font-size:14px;color:#555}
.email-row{left:79px;top:1365px;width:498px;height:42px;border-bottom:1px solid #cfd8c4}
.email-row .ph{position:absolute;left:63px;top:8px;font-size:14px;color:#555}
.video{left:698px;top:1198px;width:375px;height:250px}

/* intro */
.intro-title{left:200px;top:1558px;width:800px;text-align:center;font-size:29px;line-height:40px}
.intro-text{left:183px;top:1668px;width:834px;text-align:center;font-size:15px;line-height:26px;color:var(--text)}

/* feature rows */
.feat-title{font-family:"Poppins",sans-serif;font-weight:600;font-size:16px;line-height:26px;color:var(--ink);width:340px}
.feat-body{font-size:14.5px;line-height:26px;color:var(--text);width:390px}
.read-more{font-size:14.5px;color:var(--green)}
.right-text{text-align:right}

/* contact */
.contact{left:0;top:2787px;width:1200px;height:250px;background:var(--mint)}
.contact-col{top:2835px;width:340px;text-align:center}
.contact-icon{width:42px;height:42px;border-radius:50%;border:2px solid var(--green);margin:0 auto 16px;display:flex;align-items:center;justify-content:center}
.contact-label{font-family:"Poppins",sans-serif;font-weight:600;font-size:15px;color:var(--green)}
.contact-value{font-size:15px;line-height:27px;color:#555;margin-top:2px}
.divider{top:2833px;width:1px;height:146px;background:var(--line)}

/* footer */
.footer{left:0;top:3042px;width:1200px;height:83px;background:var(--green)}
.copyright{left:79px;top:3071px;font-size:14px;color:var(--white)}
.copyright b{font-family:"Poppins",sans-serif;font-weight:600;color:var(--ink)}
.social-foot{top:3062px;width:38px;height:38px;border-radius:50%;background:var(--ink)}
</style>
</head>
<body>

<!-- top bar -->
<div class="abs topbar-links"><span>Home</span><span class="sep">|</span><span>My Account</span><span class="sep">|</span><span>Help</span></div>
<div class="abs buy-now">
  <svg width="12" height="14" viewBox="0 0 12 14"><rect x="1" y="6" width="10" height="8" rx="1" fill="#8cc63f"/><path d="M3 6V4a3 3 0 0 1 6 0v2" fill="none" stroke="#8cc63f" stroke-width="1.6"/></svg>
  Buy Now
</div>
<div class="abs social-top" style="left:1000px"></div>
<div class="abs social-top" style="left:1036px"></div>
<div class="abs social-top" style="left:1071px"></div>
<div class="abs social-top" style="left:1108px"></div>
<div class="abs topbar-rule"></div>

<!-- nav -->
<div class="abs logo"><span class="logo-dot"></span>Petal Rush</div>
<nav class="abs nav">
  <a class="active" style="left:0">How It Works</a>
  <a style="left:116px">Delivery Areas</a>
  <a style="left:239px">Franchise</a>
  <a style="left:333px">Blog</a>
  <a style="left:389px">Free Flowers Monthly</a>
  <a style="left:560px">Corporate Arrangements</a>
</nav>
<div class="abs search">
  <svg width="18" height="18" viewBox="0 0 18 18"><circle cx="7.5" cy="7.5" r="5.2" fill="none" stroke="#1e1e1e" stroke-width="2.2"/><path d="M11.5 11.5l4.5 4.5" stroke="#1e1e1e" stroke-width="2.4" stroke-linecap="round"/></svg>
</div>

<!-- hero -->
<div class="abs hero"></div>
<div class="abs photo" role="img" aria-label="Bouquet of pink tulips with green stems" style="left:537px;top:250px;width:663px;height:469px;background:linear-gradient(135deg,#f4b6cf 0%,#e583ad 40%,#7fae4a 75%,#5f9334 100%);border-radius:60% 0 0 0/40% 0 0 0"></div>
<div class="abs photo" role="img" aria-label="Small bunch of pink daisies" style="left:0;top:546px;width:240px;height:221px;background:radial-gradient(circle at 40% 40%,#f2b7c9 0%,#dd8fab 45%,rgba(238,246,227,0) 72%)"></div>
<div class="abs script hero-title">Always Fresh</div>
<div class="abs hero-sub">Beautiful Flower Arrangements Delivered Monthly<br>Now only $69.95/MTH ($100 value)</div>
<div class="abs btn btn-fill">Free Vase</div>
<div class="abs btn btn-line">Free Upgrade</div>

<!-- three photos -->
<div class="abs photo" role="img" aria-label="Pink peonies on a wooden table" style="left:100px;top:823px;width:312px;height:208px;background:linear-gradient(135deg,#7b5a4c 0%,#d98fae 45%,#e9a9c2 65%,#6c4f45 100%)"></div>
<div class="abs photo" role="img" aria-label="Pastel rose wedding bouquet" style="left:444px;top:823px;width:312px;height:208px;background:linear-gradient(135deg,#4b4a46 0%,#c9a0b5 45%,#efe6e1 70%,#a7a39c 100%)"></div>
<div class="abs photo" role="img" aria-label="Red and pink rose bouquet held by a bride" style="left:787px;top:823px;width:313px;height:208px;background:linear-gradient(135deg,#7a1d2e 0%,#c8344f 40%,#e98aa3 70%,#f1ece6 100%)"></div>
<div class="abs script caption" style="left:100px;top:1048px">Set it and forget it</div>
<div class="abs script caption" style="left:444px;top:1048px">But never forget again</div>
<div class="abs script caption" style="left:787px;top:1048px">Making Someone's day better</div>

<!-- subscribe -->
<div class="abs subscribe"></div>
<div class="abs photo" role="img" aria-label="Pink tulips hanging from the top edge" style="left:381px;top:1135px;width:254px;height:177px;background:radial-gradient(ellipse at 50% 65%,#f0b9cb 0%,#e7a0b9 40%,rgba(238,246,227,0) 72%)"></div>
<div class="abs script sub-title">Subscribe Us!</div>
<div class="abs sub-text">Enter your email To receive a free upgrade</div>
<div class="abs email-row">
  <svg class="abs" style="left:27px;top:12px" width="20" height="14" viewBox="0 0 20 14"><rect x="1" y="1" width="18" height="12" rx="1" fill="none" stroke="#8cc63f" stroke-width="1.5"/><path d="M1 1l9 7 9-7" fill="none" stroke="#8cc63f" stroke-width="1.5"/></svg>
  <span class="ph">Enter E-mail*</span>
  <svg class="abs" style="left:455px;top:6px" width="26" height="24" viewBox="0 0 26 24"><path d="M1 11L25 1 17 23 12 14z" fill="#8cc63f"/><path d="M12 14L25 1" stroke="#eef6e3" stroke-width="1.4"/></svg>
</div>
<div class="abs video" role="img" aria-label="Video preview with a line drawing of a bouquet" style="background:linear-gradient(135deg,#b9e08c 0%,#abd678 100%)"></div>
<svg class="abs" style="left:861px;top:1299px" width="44" height="44" viewBox="0 0 44 44"><circle cx="22" cy="22" r="20" fill="#ffffff"/><circle cx="22" cy="22" r="20" fill="none" stroke="#8cc63f" stroke-width="2"/><path d="M18 14l11 8-11 8z" fill="#8cc63f"/></svg>

<!-- intro -->
<div class="abs photo" role="img" aria-label="Sprigs of lavender" style="left:0;top:1573px;width:188px;height:281px;background:radial-gradient(ellipse at 35% 40%,#6c5aa8 0%,#8a78c0 35%,rgba(255,255,255,0) 70%)"></div>
<div class="abs photo" role="img" aria-label="Two pink roses on long stems" style="left:1021px;top:1563px;width:179px;height:312px;background:radial-gradient(ellipse at 55% 35%,#eea3b8 0%,#e6a0b2 30%,#7aa061 50%,rgba(255,255,255,0) 72%)"></div>
<div class="abs script intro-title">Monthly subscription based flower delivery service in san diego<br>- CA by our florist shop</div>
<p class="abs intro-text">Every moment of life could be cherished perfectly……IF you choose wisely. To make your day more treasured, remember that flowers are the smartest choice when delivered through our monthly PetalRush subscription based delivery service. Our online subscription-based flower delivery service can help you pamper, cherish and make an everlasting impression on the minds of your loved ones with a doorstep delivery of exquisitely hand-designed floral arrangements. Our online subscription service features both standard and personalized services to help you choose from an assortment of classic and contemporary floral arrangements. It is your chance to setup a weekly, monthly, or quarterly subscription, so we can deliver the most exotic collections of hand-decorated flowers that you and your loved ones will cherish.</p>

<!-- feature row 1 -->
<div class="abs photo" role="img" aria-label="Groom holding a peach rose bouquet" style="left:177px;top:1896px;width:302px;height:156px;background:linear-gradient(135deg,#2a2f3a 0%,#4a4f5c 35%,#e7b59b 60%,#f1ddd0 100%)"></div>
<div class="abs photo" role="img" aria-label="Bride in a white gown with a bouquet" style="left:365px;top:2000px;width:197px;height:125px;background:linear-gradient(135deg,#d7cfc6 0%,#efe9e3 45%,#4b3b45 100%)"></div>
<div class="abs feat-title" style="left:658px;top:1922px">Exotic flowers garnished with special<br>hues to compliment your loved ones</div>
<div class="abs feat-body" style="left:658px;top:1983px">Let's not forget a single day in which you can make your loved ones feel special. Whether it's your anniversary or a birthday in your family,...</div>
<div class="abs read-more" style="left:658px;top:2068px">Read More &nbsp;»</div>

<!-- feature row 2 -->
<div class="abs photo" role="img" aria-label="Bunch of yellow and red tulips" style="left:0;top:2083px;width:198px;height:292px;background:radial-gradient(ellipse at 45% 45%,#f3c234 0%,#e8653b 35%,#86b04a 55%,rgba(255,255,255,0) 74%)"></div>
<div class="abs feat-title right-text" style="left:212px;top:2214px">Standard and personalized flower<br>arrangements for special occasions</div>
<div class="abs feat-body right-text" style="left:162px;top:2276px">PetalRush offers on time subscription based service that is risk free, trouble free and affordable at the same time. We offer the most trusted...</div>
<div class="abs read-more" style="left:453px;top:2360px">Read More &nbsp;»</div>
<div class="abs photo" role="img" aria-label="Table setting with pink flower centerpieces" style="left:740px;top:2187px;width:302px;height:188px;background:linear-gradient(135deg,#e9d9d4 0%,#d8a7b3 40%,#5d4a42 75%,#3c2f2a 100%)"></div>
<div class="abs photo" role="img" aria-label="Red roses with scattered petals" style="left:654px;top:2287px;width:200px;height:130px;background:linear-gradient(135deg,#8d8c8a 0%,#b01e2d 45%,#d9d4cf 100%)"></div>
<div class="abs photo" role="img" aria-label="Bunch of orange roses" style="left:1031px;top:2343px;width:169px;height:261px;background:radial-gradient(ellipse at 55% 45%,#f07a22 0%,#e85f18 35%,rgba(255,255,255,0) 70%)"></div>

<!-- feature row 3 -->
<div class="abs photo" role="img" aria-label="Mixed bouquet of roses and succulents" style="left:177px;top:2479px;width:302px;height:156px;background:linear-gradient(135deg,#3b2c27 0%,#e08a83 40%,#a8c07a 65%,#4a3a33 100%)"></div>
<div class="abs photo" role="img" aria-label="Pink peonies in a vase" style="left:365px;top:2583px;width:197px;height:125px;background:linear-gradient(135deg,#7a7c70 0%,#e49ab7 50%,#5b5e52 100%)"></div>
<div class="abs feat-title" style="left:658px;top:2505px">Get yourself subscribed and claim<br>discounts on big orders!</div>
<div class="abs feat-body" style="left:658px;top:2567px">Get love and adulation by gifting flowers to your loved ones on those special occasions. Whether it's formal, personal or your love for your family,...</div>
<div class="abs read-more" style="left:658px;top:2651px">Read More &nbsp;»</div>

<!-- contact -->
<div class="abs contact"></div>
<div class="abs photo" role="img" aria-label="Single coral rose with leaves" style="left:0;top:2718px;width:208px;height:230px;background:radial-gradient(ellipse at 45% 50%,#f26f6a 0%,#ee7d74 35%,#3f7a33 55%,rgba(238,246,227,0) 74%)"></div>
<div class="abs divider" style="left:421px"></div>
<div class="abs divider" style="left:783px"></div>

<div class="abs contact-col" style="left:70px">
  <div class="contact-icon"><svg width="18" height="18" viewBox="0 0 18 18"><path d="M4 1.5l3 3.5-1.8 2a10 10 0 0 0 5.8 5.8l2-1.8 3.5 3-2 2.5C8 16.5 1.5 10 1.5 3.5z" fill="#8cc63f"/></svg></div>
  <div class="contact-label">Call Us</div>
  <div class="contact-value">555-204-7781</div>
</div>
<div class="abs contact-col" style="left:432px">
  <div class="contact-icon"><svg width="16" height="20" viewBox="0 0 16 20"><path d="M8 1a6.5 6.5 0 0 0-6.5 6.5C1.5 12 8 19 8 19s6.5-7 6.5-11.5A6.5 6.5 0 0 0 8 1z" fill="#8cc63f"/><circle cx="8" cy="7.5" r="2.4" fill="#eef6e3"/></svg></div>
  <div class="contact-label">Address</div>
  <div class="contact-value">1840 Mesa Vista Road El Cajon, San<br>Diego CA 92021</div>
</div>
<div class="abs contact-col" style="left:790px">
  <div class="contact-icon"><svg width="20" height="14" viewBox="0 0 20 14"><rect x="0.5" y="0.5" width="19" height="13" rx="1" fill="#8cc63f"/><path d="M1 1l9 7 9-7" fill="none" stroke="#eef6e3" stroke-width="1.5"/></svg></div>
  <div class="contact-label">E-mail</div>
  <div class="contact-value">hello@petalrushsd.com</div>
</div>

<!-- footer -->
<div class="abs footer"></div>
<div class="abs copyright"><b>© PETAL RUSH - 2018.</b> All Rights Reserved.</div>
<div class="abs social-foot" style="left:958px"></div>
<div class="abs social-foot" style="left:1000px"></div>
<div class="abs social-foot" style="left:1041px"></div>
<div class="abs social-foot" style="left:1085px"></div>

</body>
</html>
```